Business Card for staff member of football club SC Brenval

I would like to get a business card template for all staff member of our soccer club.

The card should use as much as possible the 2 colors of the club : Red which is the main color and blue which is the alternative color. It can be balanced between the two like our logo.

I prefer simple and lean design.

Contact Information for Business Card

Bussiness card should have all main stuff as describe here below in must have.

Font styles to use
Sans Serif

Requirements
Must have
• Name : Laurent DESPRATIN
Fonction : Président
Mobile : +41 xx xxx xx xx
Email : first.lastname@scbrenval.ch
Adresse of the club : SC Brenval, 1873 Brenval
Website of the club : www.scbrenval.ch
Nice to have
• Version with and without picture of the staff member

A version for men, a version for women staff member.

```html
<!DOCTYPE html>
<html lang="fr">
<head>
<meta charset="utf-8">
<title>SC Brenval – Business card versions</title>
<link rel="stylesheet" href="https://fonts.googleapis.com/css2?family=Oswald:wght@300;400;500;600&display=swap">
<style>
  :root{
    --club-red:#e8243a;
    --club-red-light:#ee4a5a;
    --club-blue:#1a82c8;
    --ink:#1c1c1c;
    --white:#ffffff;
    --stage:#ebebeb;
    --photo-a:#d9c2b4;
    --photo-b:#8c6a58;
  }
  *{box-sizing:border-box;margin:0;padding:0}
  html,body{width:1200px;height:1200px;overflow:hidden}
  body{
    position:relative;
    font-family:"Oswald",sans-serif;
    background:radial-gradient(circle at 50% 50%,#fafafa 0%,var(--stage) 75%);
    color:var(--ink);
  }
  .version-title{
    position:absolute;font-weight:400;font-size:40px;line-height:1;
    letter-spacing:.2px;white-space:nowrap;
  }
  .title-plain{left:600px;top:84px;transform:translateX(-50%)}
  .title-men{right:50px;top:742px}
  .title-women{left:350px;top:1016px;transform:translateX(-50%)}

  /* Card built at 780 × 420, smaller versions scaled */
  .card{
    position:absolute;width:780px;height:420px;overflow:hidden;
    background:var(--club-red);
    color:var(--white);
    box-shadow:0 16px 14px -12px rgba(0,0,0,.35);
    transform-origin:top left;
  }
  .card-plain{left:210px;top:154px}
  .card-women{left:50px;top:687px;transform:scale(.686)}
  .card-men{left:622px;top:802px;transform:scale(.686)}

  .card-texture{
    position:absolute;inset:0;
    background:radial-gradient(ellipse at 10% 90%,var(--club-red-light) 0%,transparent 55%),
               radial-gradient(ellipse at 95% 95%,var(--club-red-light) 0%,transparent 40%);
  }
  .crest-disc{
    position:absolute;left:-30px;top:-50px;width:288px;height:288px;border-radius:50%;
    background:var(--white);
    box-shadow:6px 4px 0 0 var(--club-blue);
    display:flex;align-items:center;justify-content:center;
  }
  .card-women .crest-disc,.card-men .crest-disc{left:-40px;top:-50px;width:298px;height:298px}
  .club-name{
    font-weight:600;font-size:44px;line-height:1.05;text-align:center;
    color:var(--ink);text-transform:uppercase;margin:40px 0 0 20px;
  }

  .person{position:absolute;right:30px;text-align:right;white-space:nowrap}
  .card-plain .person{top:48px}
  .card-women .person,.card-men .person{top:140px}
  .person-name{font-weight:400;font-size:47px;line-height:1.15}
  .card-women .person-name,.card-men .person-name{font-size:44px}
  .person-role{font-weight:400;font-size:32px;line-height:1.2}

  .staff-photo{
    position:absolute;right:27px;top:13px;width:118px;height:118px;border-radius:50%;
    border:3px solid var(--white);
    background:radial-gradient(circle at 50% 40%,var(--photo-a) 0%,var(--photo-b) 100%);
  }
  .card-women .staff-photo{background:radial-gradient(circle at 50% 40%,#e6d4c8 0%,#5a3d30 100%)}

  .contact{
    position:absolute;display:flex;align-items:center;gap:16px;
    font-weight:300;font-size:30px;line-height:1;white-space:nowrap;
  }
  .contact-left{left:22px}
  .contact-right{right:30px}
  .row-1{top:282px}
  .row-2{top:338px}
  .contact-right.row-1 .contact-text{font-size:27px}
  .contact-right.row-2 .contact-text{font-size:28px}
  .icon{
    width:44px;height:44px;border-radius:50%;flex:none;
    background:var(--club-blue);display:flex;align-items:center;justify-content:center;
  }
  .icon svg{width:24px;height:24px;fill:none;stroke:var(--white);stroke-width:1.6;stroke-linecap:round;stroke-linejoin:round}
</style>
</head>
<body>

<h2 class="version-title title-plain">Version without staff Picture</h2>
<h2 class="version-title title-men">Version with men staff Picture</h2>
<h2 class="version-title title-women">Version with women staff Picture</h2>

<!-- Card without photo -->
<article class="card card-plain">
  <div class="card-texture" role="img" aria-label="Soft dotted club pattern background"></div>
  <div class="crest-disc"><p class="club-name">SC<br>Brenval</p></div>
  <div class="person">
    <p class="person-name">Laurent DESPRATIN</p>
    <p class="person-role">Président</p>
  </div>
  <p class="contact contact-left row-1">
    <span class="icon"><svg viewBox="0 0 24 24"><path d="M12 21s-6-6.2-6-11a6 6 0 0 1 12 0c0 4.8-6 11-6 11z"/><circle cx="12" cy="10" r="2.2"/></svg></span>
    <span class="contact-text">SC Brenval, 1873 Brenval</span>
  </p>
  <p class="contact contact-left row-2">
    <span class="icon"><svg viewBox="0 0 24 24"><circle cx="12" cy="12" r="9"/><path d="M3 12h18M12 3c3 3.2 3 14.8 0 18M12 3c-3 3.2-3 14.8 0 18"/></svg></span>
    <span class="contact-text">www.scbrenval.ch</span>
  </p>
  <p class="contact contact-right row-1">
    <span class="icon"><svg viewBox="0 0 24 24"><path d="M5 4h4l2 5-2.5 1.5a11 11 0 0 0 5 5L15 13l5 2v4a2 2 0 0 1-2 2A16 16 0 0 1 3 6a2 2 0 0 1 2-2z"/></svg></span>
    <span class="contact-text">+41 xx xxx xx xx</span>
  </p>
  <p class="contact contact-right row-2">
    <span class="icon"><svg viewBox="0 0 24 24"><rect x="3" y="6" width="18" height="12" rx="1.5"/><path d="M3 7l9 6 9-6"/></svg></span>
    <span class="contact-text">first.lastname@scbrenval.ch</span>
  </p>
</article>

<!-- Card with women staff photo -->
<article class="card card-women">
  <div class="card-texture" role="img" aria-label="Soft dotted club pattern background"></div>
  <div class="crest-disc"><p class="club-name">SC<br>Brenval</p></div>
  <div class="staff-photo" role="img" aria-label="Portrait photo of the female staff member"></div>
  <div class="person">
    <p class="person-name">Laurent DESPRATIN</p>
    <p class="person-role">Président</p>
  </div>
  <p class="contact contact-left row-1">
    <span class="icon"><svg viewBox="0 0 24 24"><path d="M12 21s-6-6.2-6-11a6 6 0 0 1 12 0c0 4.8-6 11-6 11z"/><circle cx="12" cy="10" r="2.2"/></svg></span>
    <span class="contact-text">SC Brenval, 1873 Brenval</span>
  </p>
  <p class="contact contact-left row-2">
    <span class="icon"><svg viewBox="0 0 24 24"><circle cx="12" cy="12" r="9"/><path d="M3 12h18M12 3c3 3.2 3 14.8 0 18M12 3c-3 3.2-3 14.8 0 18"/></svg></span>
    <span class="contact-text">www.scbrenval.ch</span>
  </p>
  <p class="contact contact-right row-1">
    <span class="icon"><svg viewBox="0 0 24 24"><path d="M5 4h4l2 5-2.5 1.5a11 11 0 0 0 5 5L15 13l5 2v4a2 2 0 0 1-2 2A16 16 0 0 1 3 6a2 2 0 0 1 2-2z"/></svg></span>
    <span class="contact-text">+41 xx xxx xx xx</span>
  </p>
  <p class="contact contact-right row-2">
    <span class="icon"><svg viewBox="0 0 24 24"><rect x="3" y="6" width="18" height="12" rx="1.5"/><path d="M3 7l9 6 9-6"/></svg></span>
    <span class="contact-text">first.lastname@scbrenval.ch</span>
  </p>
</article>

<!-- Card with men staff photo -->
<article class="card card-men">
  <div class="card-texture" role="img" aria-label="Soft dotted club pattern background"></div>
  <div class="crest-disc"><p class="club-name">SC<br>Brenval</p></div>
  <div class="staff-photo" role="img" aria-label="Portrait photo of the male staff member"></div>
  <div class="person">
    <p class="person-name">Laurent DESPRATIN</p>
    <p class="person-role">Président</p>
  </div>
  <p class="contact contact-left row-1">
    <span class="icon"><svg viewBox="0 0 24 24"><path d="M12 21s-6-6.2-6-11a6 6 0 0 1 12 0c0 4.8-6 11-6 11z"/><circle cx="12" cy="10" r="2.2"/></svg></span>
    <span class="contact-text">SC Brenval, 1873 Brenval</span>
  </p>
  <p class="contact contact-left row-2">
    <span class="icon"><svg viewBox="0 0 24 24"><circle cx="12" cy="12" r="9"/><path d="M3 12h18M12 3c3 3.2 3 14.8 0 18M12 3c-3 3.2-3 14.8 0 18"/></svg></span>
    <span class="contact-text">www.scbrenval.ch</span>
  </p>
  <p class="contact contact-right row-1">
    <span class="icon"><svg viewBox="0 0 24 24"><path d="M5 4h4l2 5-2.5 1.5a11 11 0 0 0 5 5L15 13l5 2v4a2 2 0 0 1-2 2A16 16 0 0 1 3 6a2 2 0 0 1 2-2z"/></svg></span>
    <span class="contact-text">+41 xx xxx xx xx</span>
  </p>
  <p class="contact contact-right row-2">
    <span class="icon"><svg viewBox="0 0 24 24"><rect x="3" y="6" width="18" height="12" rx="1.5"/><path d="M3 7l9 6 9-6"/></svg></span>
    <span class="contact-text">first.lastname@scbrenval.ch</span>
  </p>
</article>

</body>
</html>
```